Employee Portal UI Design - Modern and Clean

We are an agency tasked with developing a team portal for a company that has many employees. As we embark on this project, we seek a great UI design to accompany the requirements our client has for this project. We already have several screens mocked up that can be used as reference for the overall idea. Currently, we are only looking for the main dashboard's home page, user registration screen, and account settings page to be designed. The main brand colors are red but other accents can be used as well. The client's vision is for modern & minimalist to be at the center. We have a specific font to be used, but if you don't have access to it, you can just use a similar font.Main color: #DD0031The sub menus (do not need to be designed) would be:>Performance Reviews>Posts>Team directory>Calendar>Tasks>Documents>LinksWe would prefer the design be made in Adobe XD.

Industry/Entity Type

Fast Food Restaurant

Number of Pages Required

1 page

Font styles to use
Sans Serif

Colors
ec1f27

Requirements
Must have
• Color: #DD0031 (highlights)

```html
<!DOCTYPE html>
<html lang="en">
<head>
<meta charset="utf-8">
<title>Crewhub – Home</title>
<link href="https://fonts.googleapis.com/css2?family=Roboto:wght@300;400;500;700&display=swap" rel="stylesheet">
<style>
:root{
  --brand:#DD0031;
  --bar:#e03236;
  --ink:#333333;
  --muted:#8a8a8a;
  --line:#e2e2e2;
  --nav-active:#444444;
  --blue:#2f6fd6;
  --bg:#ffffff;
}
*{margin:0;padding:0;box-sizing:border-box}
html,body{width:1200px;height:675px;overflow:hidden;background:var(--bg);font-family:'Roboto',sans-serif;color:var(--ink)}
.app{position:relative;width:1200px;height:675px}
.abs{position:absolute}

/* sidebar */
.sidebar{left:0;top:0;width:240px;height:675px;border-right:1px solid var(--line);background:#fff}
.brand{left:30px;top:20px;font-size:40px;font-weight:400;color:var(--ink);letter-spacing:.5px;line-height:1}
.profile-photo{left:31px;top:92px;width:70px;height:70px;border-radius:50%;background:radial-gradient(circle at 50% 40%,#b58d75,#5b4a41)}
.profile-name{left:110px;top:118px;font-size:14.5px;font-weight:300;color:var(--ink);display:flex;align-items:center;gap:9px}
.nav{left:0;top:183px;width:240px;list-style:none}
.nav li{position:relative;height:51px;display:flex;align-items:center;padding-left:63px;font-size:15px;font-weight:300;color:var(--ink);margin-bottom:6px}
.nav li svg{position:absolute;left:30px;width:20px;height:20px;fill:#444}
.nav li.active{background:var(--nav-active);color:#fff;font-weight:400;margin-bottom:6px}
.nav li.active::before{content:"";position:absolute;left:0;top:0;bottom:0;width:4px;background:var(--brand)}
.nav li.active svg{fill:#fff}

/* header */
.topbar{left:240px;top:0;width:960px;height:89px;background:var(--bar)}
.menu-btn{left:267px;top:34px}
.search{left:321px;top:25px;width:282px;height:38px;background:#fff;border-radius:19px;display:flex;align-items:center;padding-left:13px;gap:9px;font-size:15px;font-weight:300;color:#888}
.bell{left:1061px;top:30px}
.gear{left:1129px;top:30px}

/* activity feed */
.section-title{font-size:18px;font-weight:400;color:var(--ink)}
.btn{background:var(--bar);color:#fff;border-radius:17px;display:flex;align-items:center;justify-content:center;font-size:11px;box-shadow:0 2px 4px rgba(0,0,0,.2)}
.btn-new{left:825px;top:110px;width:93px;height:33px;gap:12px}
.post{left:262px;width:657px;height:142px;border:1px solid var(--line);border-radius:4px;box-shadow:0 1px 4px rgba(0,0,0,.12);background:#fff}
.post .avatar{left:21px;top:12px;width:38px;height:38px;border-radius:50%;background:radial-gradient(circle at 50% 40%,#b58d75,#5b4a41)}
.post .author{left:66px;top:15px;font-size:14.5px;color:var(--bar);font-weight:400;line-height:1}
.post .visibility{left:66px;top:34px;font-size:11px;font-weight:700;color:var(--ink)}
.post .divider{left:162px;top:13px;width:1px;height:36px;background:var(--line)}
.post .subject{left:177px;top:22px;font-size:15px;font-weight:300}
.post .time{right:22px;top:30px;font-size:11px;font-weight:700;display:flex;align-items:center;gap:5px}
.post .body{left:20px;top:58px;width:620px;font-size:14.5px;font-weight:300;line-height:25.5px}
.read-more{color:var(--bar);font-weight:700;float:right}

/* events */
.panel{left:945px;width:226px;border:1px solid var(--line);border-radius:3px;box-shadow:0 1px 4px rgba(0,0,0,.12);background:#fff}
.events{top:111px;height:320px}
.tab{top:14px;font-size:18px;font-weight:400}
.tab-active{left:28px;color:var(--ink)}
.tab-idle{left:142px;color:#b5b5b5;font-weight:300}
.tab-line{left:0;top:47px;width:113px;height:2px;background:var(--bar)}
.event{left:21px;width:188px}
.event .title{font-size:15px;padding-left:18px;position:relative;line-height:1}
.event .title::before{content:"";position:absolute;left:1px;top:4px;width:9px;height:9px;border-radius:50%}
.event.red .title{color:var(--bar)}.event.red .title::before{background:var(--bar)}
.event.blue .title{color:var(--blue)}.event.blue .title::before{background:var(--blue)}
.event .meta{padding-left:20px;font-size:10.5px;font-weight:300;line-height:16px;margin-top:4px}
.event .meta .sep{display:inline-block;width:1px;height:12px;background:#777;vertical-align:-2px;margin:0 3px}
.rule{left:19px;width:188px;height:1px;background:var(--line)}
.link-all{left:0;width:100%;text-align:center;font-size:15px;font-weight:700;color:var(--bar)}

/* polls */
.polls-title{left:948px;top:444px}
.poll{top:474px;height:179px}
.poll .question{left:22px;top:15px;font-size:11px;font-weight:300}
.poll .opt-bar{left:22px;top:36px;width:3px;height:27px;background:var(--bar)}
.poll .opt{left:35px;font-size:11px}
.opt-selected{top:43px;color:var(--bar);font-weight:700}
.opt-plain{top:70px;font-weight:300}
.btn-vote{left:64px;top:95px;width:93px;height:33px;font-size:11px}
</style>
</head>
<body>
<div class="app">

  <aside class="sidebar abs">
    <div class="brand abs">Crewhub</div>
    <div class="profile-photo abs" role="img" aria-label="Profile photo of Daniel Reyes"></div>
    <div class="profile-name abs">Daniel Reyes
      <svg width="10" height="6" viewBox="0 0 10 6"><path d="M0 0h10L5 6z" fill="#333"/></svg>
    </div>
    <ul class="nav abs">
      <li class="active"><svg viewBox="0 0 20 20"><path d="M10 2 1 10h3v8h4.5v-5h3v5H16v-8h3z"/></svg>Home</li>
      <li><svg viewBox="0 0 20 20"><rect x="1" y="11" width="3" height="7"/><rect x="6" y="4" width="3" height="14"/><rect x="11" y="8" width="3" height="10"/><rect x="16" y="12" width="3" height="6"/></svg>Performance Reviews</li>
      <li><svg viewBox="0 0 20 20"><path d="M10 1 1 5.5 10 10l9-4.5z"/><path d="M2.8 8.6 1 9.5 10 14l9-4.5-1.8-.9L10 12.2z"/><path d="M2.8 12.6 1 13.5 10 18l9-4.5-1.8-.9L10 16.2z"/></svg>Posts</li>
      <li><svg viewBox="0 0 20 20"><circle cx="10" cy="6" r="3"/><circle cx="4" cy="7" r="2.3"/><circle cx="16" cy="7" r="2.3"/><path d="M5 16c0-4 2-6 5-6s5 2 5 6z"/><path d="M0 15c0-3 1.5-4.5 4-4.5 1 0 1.6.2 2 .6C4.8 12.3 4.2 13.6 4.1 15z"/><path d="M20 15c0-3-1.5-4.5-4-4.5-1 0-1.6.2-2 .6 1.2 1.2 1.8 2.5 1.9 3.9z"/></svg>Team Directory</li>
      <li><svg viewBox="0 0 20 20"><path d="M1 3h18v16H1zm2 5v9h14V8z"/><rect x="5" y="1" width="2" height="4"/><rect x="13" y="1" width="2" height="4"/></svg>Calendar</li>
      <li><svg viewBox="0 0 20 20"><rect x="1" y="4" width="18" height="1.5"/><rect x="1" y="9.5" width="18" height="1.5"/><rect x="1" y="15" width="18" height="1.5"/><rect x="12" y="2.5" width="2" height="4.5"/><rect x="5" y="8" width="2" height="4.5"/><rect x="10" y="13.5" width="2" height="4.5"/></svg>Tasks</li>
      <li><svg viewBox="0 0 20 20"><path d="M1 3h14v2H3v12H1z"/><rect x="4" y="6" width="15" height="12"/></svg>Documents</li>
      <li><svg viewBox="0 0 20 20"><path d="M6 6h4a4 4 0 0 1 0 8H8v-2.4h2a1.6 1.6 0 0 0 0-3.2H6a1.6 1.6 0 0 0 0 3.2h.5V14H6a4 4 0 0 1 0-8z"/><path d="M14 14h-4v-2.4h4a1.6 1.6 0 0 0 0-3.2h-.5V6h.5a4 4 0 0 1 0 8z"/></svg>Links</li>
    </ul>
  </aside>

  <header class="topbar abs"></header>
  <svg class="menu-btn abs" width="30" height="22" viewBox="0 0 30 22"><rect y="1" width="30" height="3" fill="#fff"/><rect y="9" width="30" height="3" fill="#fff"/><rect y="17" width="30" height="3" fill="#fff"/></svg>
  <div class="search abs">
    <svg width="24" height="24" viewBox="0 0 24 24"><circle cx="10" cy="10" r="7.5" fill="none" stroke="#777" stroke-width="2"/><path d="m15.5 15.5 6 6" stroke="#777" stroke-width="2.4"/></svg>
    Search
  </div>
  <svg class="bell abs" width="34" height="32" viewBox="0 0 34 32"><path d="M15 4c-5 0-8 4-8 9v6l-3 4h22l-3-4v-6c0-5-3-9-8-9z" fill="none" stroke="#fff" stroke-width="2"/><path d="M12 25a3 3 0 0 0 6 0" fill="none" stroke="#fff" stroke-width="2"/><circle cx="26" cy="9" r="6" fill="#fff"/><text x="26" y="12.5" font-size="9" text-anchor="middle" fill="#e03236" font-family="Roboto,sans-serif">1</text></svg>
  <svg class="gear abs" width="30" height="30" viewBox="0 0 24 24"><path fill="#fff" d="M19.4 13a7.5 7.5 0 0 0 0-2l2.1-1.6-2-3.5-2.5 1a7.6 7.6 0 0 0-1.7-1L15 3h-4l-.4 2.7a7.6 7.6 0 0 0-1.7 1l-2.5-1-2 3.5L6.6 11a7.5 7.5 0 0 0 0 2l-2.1 1.6 2 3.5 2.5-1a7.6 7.6 0 0 0 1.7 1L11 21h4l.4-2.7a7.6 7.6 0 0 0 1.7-1l2.5 1 2-3.5zM13 15.5a3.5 3.5 0 1 1 0-7 3.5 3.5 0 0 1 0 7z"/></svg>

  <main>
    <h1 class="section-title abs" style="left:265px;top:119px">Recent Activites</h1>
    <div class="btn btn-new abs">New
      <svg width="12" height="12" viewBox="0 0 12 12"><path d="M5 0h2v5h5v2H7v5H5V7H0V5h5z" fill="#fff"/></svg>
    </div>

    <article class="post abs" style="top:164px">
      <div class="avatar abs" role="img" aria-label="Author photo"></div>
      <div class="author abs">Daniel Reyes</div>
      <div class="visibility abs">Public</div>
      <div class="divider abs"></div>
      <div class="subject abs">Post Subject Message</div>
      <div class="time abs"><svg width="12" height="12" viewBox="0 0 12 12"><circle cx="6" cy="6" r="5.3" fill="none" stroke="#777"/><path d="M6 3v3H4" fill="none" stroke="#777"/></svg>Today, 1:43</div>
      <p class="body abs">Lorem ipsum dolor sit amet, paulo soleat ex sed. Discere perpetua tincidunt mel ea, mel vocent dissentiunt ut, duis aeque mucius vis ex. Eros ipsum causae ex vis, ad eos nostrud ponderum. Ea nonumy accommodare vel, te nullam docendi theophrastus mea. <span class="read-more">Read More</span></p>
    </article>

    <article class="post abs" style="top:337px">
      <div class="avatar abs" role="img" aria-label="Author photo"></div>
      <div class="author abs">Daniel Reyes</div>
      <div class="visibility abs">Public</div>
      <div class="divider abs"></div>
      <div class="subject abs">Post Subject Message</div>
      <div class="time abs"><svg width="12" height="12" viewBox="0 0 12 12"><circle cx="6" cy="6" r="5.3" fill="none" stroke="#777"/><path d="M6 3v3H4" fill="none" stroke="#777"/></svg>Today, 1:43</div>
      <p class="body abs">Lorem ipsum dolor sit amet, paulo soleat ex sed. Discere perpetua tincidunt mel ea, mel vocent dissentiunt ut, duis aeque mucius vis ex. Eros ipsum causae ex vis, ad eos nostrud ponderum. Ea nonumy accommodare vel, te nullam docendi theophrastus mea. <span class="read-more">Read More</span></p>
    </article>

    <article class="post abs" style="top:511px">
      <div class="avatar abs" role="img" aria-label="Author photo"></div>
      <div class="author abs">Daniel Reyes</div>
      <div class="visibility abs">Public</div>
      <div class="divider abs"></div>
      <div class="subject abs">Post Subject Message</div>
      <div class="time abs"><svg width="12" height="12" viewBox="0 0 12 12"><circle cx="6" cy="6" r="5.3" fill="none" stroke="#777"/><path d="M6 3v3H4" fill="none" stroke="#777"/></svg>Today, 1:43</div>
      <p class="body abs">Lorem ipsum dolor sit amet, paulo soleat ex sed. Discere perpetua tincidunt mel ea, mel vocent dissentiunt ut, duis aeque mucius vis ex. Eros ipsum causae ex vis, ad eos nostrud ponderum. Ea nonumy accommodare vel, te nullam docendi theophrastus mea. <span class="read-more">Read More</span></p>
    </article>
  </main>

  <section class="panel events abs">
    <div class="tab tab-active abs">Events</div>
    <div class="tab tab-idle abs">Tasks</div>
    <div class="tab-line abs"></div>

    <div class="event red abs" style="top:68px">
      <div class="title">Director Meeting</div>
      <div class="meta">18 Jan, Thu<span class="sep"></span>10:00 am - 11:00 am<br>Restaurant</div>
    </div>
    <div class="rule abs" style="top:125px"></div>
    <div class="event blue abs" style="top:139px">
      <div class="title">Free Breakfast</div>
      <div class="meta">18 Jan, Thu<span class="sep"></span>06:30 am - 10:00 am<br>Restaurant</div>
    </div>
    <div class="rule abs" style="top:201px"></div>
    <div class="event blue abs" style="top:215px">
      <div class="title">Daddy Daughter Night</div>
      <div class="meta">18 Jan, Thu<span class="sep"></span>06:30 am - 10:00 am<br>Restaurant</div>
    </div>
    <div class="rule abs" style="top:274px"></div>
    <div class="link-all abs" style="top:288px">View All Events</div>
  </section>

  <h2 class="section-title polls-title abs">Polls</h2>
  <section class="panel poll abs">
    <div class="question abs">What is your favorite enteree?</div>
    <div class="opt-bar abs"></div>
    <div class="opt opt-selected abs">Classic Chicken Sandwich</div>
    <div class="opt opt-plain abs">Chicken Strips</div>
    <div class="btn btn-vote abs">Submit Vote</div>
    <div class="rule abs" style="top:138px"></div>
    <div class="link-all abs" style="top:148px">View All Polls</div>
  </section>

</div>
</body>
</html>
```